A land page lead collector for people who want to reduce there postage costs

We are looking to create a single page website landing page to collect leads of people who want to reduce there postage costs.

The form should basically ask:

Name:
Business Name:
Address:
Town:
Post Code:
Email:
Phone:
Letter Volume Per Week:
Parcel Volume Per Week:

We should basically be advertising cheaper postage costs.

We will not be showing prices on this website we will just be collecting the leads.

Our competition website is as follows https://mailfernquest.com

But we are not a online service. This is just a collector to get leads of people who want to save money on there postage costs.
Updates

Target Market(s)

Small and medium sized enterprises

Industry/Entity Type

Advertising

Number of Pages Required

1 page

Colors
ec2027
0356a4

Requirements
Must have
• Form above the fold of the page
Nice to have
• Colour red and blue.
• Parallax design would be nice.

```html
<!DOCTYPE html>
<html lang="en">
<head>
<meta charset="utf-8">
<title>Quick Signup – Cheaper Postage</title>
<link rel="stylesheet" href="https://fonts.googleapis.com/css2?family=Montserrat:wght@300;400&family=Nunito+Sans:wght@400;600&family=Oswald:wght@500&display=swap">
<style>
  :root {
    --red: #ec2027;
    --red-panel: rgba(236, 32, 39, 0.82);
    --blue: #0356a4;
    --blue-soft: #6f9fd3;
    --white: #ffffff;
    --field: #f4f4f4;
    --ink: #333333;
  }
  * { box-sizing: border-box; margin: 0; padding: 0; }
  html, body { width: 1200px; height: 845px; overflow: hidden; }
  body { position: relative; font-family: "Nunito Sans", sans-serif; background: var(--white); }

  .hero-photo {
    position: absolute; left: 0; top: 0; width: 1200px; height: 750px;
    background:
      radial-gradient(ellipse at 78% 45%, rgba(255,255,255,0.55), rgba(255,255,255,0) 55%),
      linear-gradient(90deg, #a8969a 0%, #8c7b78 30%, #4e4340 48%, #6b5d58 60%, #c9c3c0 80%, #dcd8d6 100%);
  }

  .signup-panel {
    position: absolute; left: 98px; top: 0; width: 368px; height: 750px;
    background: var(--red-panel);
  }
  .free-ribbon {
    position: absolute; left: 0; top: 0; width: 74px; height: 98px;
    background: var(--blue);
    clip-path: polygon(0 0, 100% 0, 100% 100%, 50% 90%, 0 100%);
    color: var(--white); text-align: center;
  }
  .free-ribbon .pct { display: block; margin-top: 13px; font-size: 13px; line-height: 16px; opacity: .85; }
  .free-ribbon .free { display: block; font-family: "Oswald", sans-serif; font-size: 25px; line-height: 28px; letter-spacing: .5px; }
  .free-ribbon .soon { display: block; font-size: 13px; line-height: 16px; opacity: .85; }

  .envelope-icon { position: absolute; left: 154px; top: 84px; width: 64px; height: 68px; }
  .signup-title {
    position: absolute; left: 0; top: 160px; width: 368px; text-align: center;
    font-family: "Montserrat", sans-serif; font-weight: 300; color: var(--white);
    font-size: 24px; line-height: 28px;
  }
  .signup-sub {
    position: absolute; left: 0; top: 185px; width: 368px; text-align: center;
    font-family: "Montserrat", sans-serif; font-weight: 300; color: var(--white);
    font-size: 13px; line-height: 16px;
  }

  .signup-form { position: absolute; left: 47px; top: 219px; width: 272px; }
  .field {
    position: relative; height: 35px; margin-bottom: 3px;
    background: linear-gradient(var(--field), var(--white));
    border-bottom: 2px solid #c8161d;
    color: var(--ink); font-size: 12.5px; line-height: 33px; padding-left: 12px;
  }
  .field.select::after {
    content: ""; position: absolute; right: 0; top: 0; width: 29px; height: 35px;
    background: var(--blue-soft);
  }
  .field.select .chevron { position: absolute; right: 10px; top: 13px; width: 9px; height: 6px; z-index: 1; }
  .submit-btn {
    display: block; margin-top: 19px; width: 272px; height: 35px;
    background: var(--blue); color: var(--white); text-align: center;
    font-size: 12.5px; line-height: 35px; box-shadow: 0 2px 3px rgba(0,0,0,.2);
  }

  .social-links { position: absolute; left: 1012px; top: 34px; display: flex; gap: 10px; }
  .social-link { display: flex; align-items: center; gap: 4px; color: var(--white); font-size: 11px; }
  .social-link .dot { width: 10px; height: 10px; border: 1.5px solid var(--white); border-radius: 50%; }

  .headline {
    position: absolute; left: 580px; top: 340px; width: 440px;
    font-family: "Montserrat", sans-serif; font-weight: 300; color: var(--white);
    font-size: 40px; line-height: 52px;
  }
  .cta-btn {
    position: absolute; left: 581px; top: 514px; width: 272px; height: 36px;
    background: var(--blue); color: var(--white); text-align: center;
    font-size: 12.5px; line-height: 36px;
  }
  .slide-next { position: absolute; left: 1014px; top: 464px; width: 38px; height: 38px; }

  .site-footer {
    position: absolute; left: 0; top: 750px; width: 1200px; height: 95px;
    background: var(--blue);
  }
  .copyright {
    position: absolute; left: 98px; top: 44px; color: var(--white);
    font-family: Arial, sans-serif; font-size: 15px;
  }
</style>
</head>
<body>
  <div class="hero-photo" role="img" aria-label="Photo of a woman smiling as she opens a cardboard parcel filled with bubble wrap, bookshelves blurred behind her"></div>

  <section class="signup-panel">
    <div class="free-ribbon">
      <span class="pct">– 100% –</span>
      <span class="free">FREE</span>
      <span class="soon">– Soon –</span>
    </div>

    <svg class="envelope-icon" viewBox="0 0 64 68" aria-hidden="true">
      <path d="M0 26 L32 0 L64 26 L64 68 L0 68 Z" fill="var(--white)"/>
      <path d="M0 26 L32 48 L64 26" fill="none" stroke="var(--red)" stroke-width="2.5"/>
      <path d="M0 68 L26 44 M64 68 L38 44" fill="none" stroke="var(--red)" stroke-width="2.5"/>
    </svg>

    <h1 class="signup-title">Quick Signup</h1>
    <p class="signup-sub">lorem ipsum dolor sit amet</p>

    <form class="signup-form">
      <div class="field">Name</div>
      <div class="field">Business Name</div>
      <div class="field">Address</div>
      <div class="field">Post Code</div>
      <div class="field select">Town
        <svg class="chevron" viewBox="0 0 9 6"><path d="M1 1 L4.5 4.5 L8 1" fill="none" stroke="#fff" stroke-width="1.8"/></svg></div>
      <div class="field">Phone</div>
      <div class="field">Email</div>
      <div class="field select">Letter Volume Per Week
        <svg class="chevron" viewBox="0 0 9 6"><path d="M1 1 L4.5 4.5 L8 1" fill="none" stroke="#fff" stroke-width="1.8"/></svg></div>
      <div class="field select">Parcel Volume Per Week
        <svg class="chevron" viewBox="0 0 9 6"><path d="M1 1 L4.5 4.5 L8 1" fill="none" stroke="#fff" stroke-width="1.8"/></svg></div>
      <div class="submit-btn">Submit Now</div>
    </form>
  </section>

  <nav class="social-links">
    <span class="social-link"><span class="dot"></span>Hiveo</span>
    <span class="social-link"><span class="dot"></span>Linkra</span>
    <span class="social-link"><span class="dot"></span>Mesho</span>
  </nav>

  <h2 class="headline">Lorem ipsum dolor sit amet, consectetur adipisicing</h2>
  <div class="cta-btn">Click to Get in Touch</div>

  <svg class="slide-next" viewBox="0 0 38 38" aria-label="Next slide">
    <circle cx="19" cy="19" r="19" fill="rgba(255,255,255,0.35)"/>
    <path d="M16 12 L23 19 L16 26" fill="none" stroke="#fff" stroke-width="3"/>
  </svg>

  <footer class="site-footer">
    <p class="copyright">Copyright © 2015</p>
  </footer>
</body>
</html>
```